Letterhead Design Project

Brightwater Advisory is a newly created boutique consultancy focussing on delivering strategic consulting to medium and large businesses, with a focus on:
- Strategic planning and execution.
- Corporate function optimisation, especially in the areas of finance, commercial, and IT. This includes implementing the right functional design for the needs of the business, and ensuring the right skills.
- Performance management, in particular project governance and control, operational metrics and management reporting.
I have in mind a tag line for the business being:
"Helping business to discover sustainable value."
I am looking for a letterhead design which utilises my new logo on report templates (powerpoint and word), and letterhead.
Knowlepedex defines a mother lode as follows:
"Mother lode is a principal vein or zone of veins of gold or silver ore. The term probably came from a literal translation of the Spanish veta madre, a term common in old Mexican mining. Veta madre, for instance, is the name given to an 11-kilometre-long (6.8 mi) silver vein discovered in 1548 in Guanajuato, New Spain (modern-day Mexico)."
My preference is for black and gold. Logo files are attached in .eps format. All fonts are outlined. The fonts that are used are "Crimson Text" and "Josefin Sans". They are free open source fonts and they are available here: http://www.typorama-lib.example/fonts
Target Market(s)
Medium to large corporates.
Industry/Entity Type
Boutique
Font styles to use
Other font styles liked:
- All fonts are outlined. The fonts that are used are "Crimson Text" and "Josefin Sans". They are free open source fonts and they are available here: http://www.typorama-lib.example/fonts
Look and feel
Each slider illustrates characteristics of the customer's brand and the style your logo design should communicate.

```html
<!DOCTYPE html>
<html lang="en">
<head>
<meta charset="utf-8">
<title>Brightwater Advisory – Letterhead</title>
<link rel="stylesheet" href="https://fonts.googleapis.com/css2?family=Crimson+Text:wght@400;600&family=Josefin+Sans:wght@400;600&display=swap">
<style>
  :root {
    --backdrop: #a9a9a9;
    --paper: #f3f3f4;
    --ink: #1c1c1c;
    --gold: #d9a933;
    --muted: #444;
    --signature-tone: #d6d6d6;
  }
  * { box-sizing: border-box; margin: 0; padding: 0; }
  html, body { width: 1200px; height: 1143px; overflow: hidden; }
  body {
    background: radial-gradient(ellipse at 40% 20%, #d2d2d2, var(--backdrop));
    display: flex; align-items: center; justify-content: center;
    font-family: "Josefin Sans", sans-serif; color: var(--ink);
  }
  .letterhead {
    position: relative; width: 760px; height: 1075px;
    background: var(--paper);
    box-shadow: 0 12px 30px rgba(0,0,0,.25);
    padding: 90px 80px 0 80px;
  }
  .brand {
    position: absolute; top: 96px; right: 80px;
  }
  .brand-name {
    font-family: "Crimson Text", serif; font-weight: 400;
    font-size: 36px; letter-spacing: 1px; color: var(--ink);
    white-space: nowrap;
  }
  .letter-body {
    margin-top: 150px; font-size: 17px; line-height: 1.5; color: var(--ink);
  }
  .letter-body p { text-indent: 40px; margin-bottom: 24px; }
  .signature { margin-top: 90px; margin-left: 300px; }
  .signature-name { font-size: 20px; font-weight: 600; }
  .signature-mark { width: 70px; height: 22px; margin-top: 4px; background: var(--signature-tone); border-radius: 3px; }
  .letter-footer {
    position: absolute; left: 80px; right: 80px; bottom: 60px;
    border-top: 2px solid var(--gold); padding-top: 14px;
    display: flex; justify-content: space-between; align-items: flex-start;
    gap: 16px; font-size: 13px; color: var(--muted);
  }
  .contact-item { display: flex; align-items: center; gap: 6px; margin-bottom: 6px; white-space: nowrap; }
  .contact-item svg { width: 13px; height: 13px; flex: none; }
</style>
</head>
<body>
<main class="letterhead">
  <header class="brand">
    <span class="brand-name">Brightwater Advisory</span>
  </header>

  <section class="letter-body">
    <p>Lorem ipsum dolor sit amet, consectetuer adipiscing elit, sed diam nonummy nibh euismod tincidunt ut laoreet dolore magna aliquam erat volutpat. Ut wisi enim ad minim veniam, quis nostrud exerci tation ullamcorper suscipit lobortis nisl ut aliquip ex ea commodo consequat.</p>
    <p>Duis autem vel eum iriure dolor in hendrerit in vulputate velit esse molestie consequat, vel illum dolore eu feugiat nulla facilisis at vero eros et accumsan et iusto odio dignissim qui blandit praesent luptatum zzril delenit augue duis dolore te feugait nulla facilisi. Nam liber tempor cum soluta nobis eleifend option congue nihil imperdiet doming id quod mazim placerat facer possim assum. Typi non habent claritatem insitam; est usus legentis in iis qui facit eorum claritatem. Investigationes demonstraverunt lectores legere me lius quod ii legunt saepius.</p>
    <p>Claritas est etiam processus dynamicus, qui sequitur mutationem consuetudium lectorum. Mirum est notare quam littera gothica, quam nunc putamus parum claram, anteposuerit litterarum formas humanitatis per seacula quarta decima et quinta decima. Eodem modo typi, qui nunc nobis videntur parum clari, fiant sollemnes in futurum.</p>
  </section>

  <div class="signature">
    <div class="signature-name">John Doe</div>
    <div class="signature-mark" role="img" aria-label="Handwritten signature"></div>
  </div>

  <footer class="letter-footer">
    <div class="contact-group">
      <div class="contact-item">
        <svg viewBox="0 0 14 14"><path d="M7 1a4 4 0 0 0-4 4c0 3 4 8 4 8s4-5 4-8a4 4 0 0 0-4-4z" fill="none" stroke="var(--gold)" stroke-width="1.5"/><circle cx="7" cy="5" r="1.4" fill="var(--gold)"/></svg>
        Quarry Lane 88, Ridgeford 4567, Australia
      </div>
      <div class="contact-item">
        <svg viewBox="0 0 14 14"><circle cx="7" cy="7" r="5.5" fill="none" stroke="var(--gold)" stroke-width="1.5"/><circle cx="7" cy="7" r="2" fill="none" stroke="var(--gold)" stroke-width="1.5"/></svg>
        hello@brightwater.example
      </div>
    </div>
    <div class="contact-item">
      <svg viewBox="0 0 14 14"><circle cx="7" cy="7" r="5.5" fill="none" stroke="var(--gold)" stroke-width="1.5"/><path d="M1.5 7h11M7 1.5c-3 3-3 8 0 11M7 1.5c3 3 3 8 0 11" fill="none" stroke="var(--gold)" stroke-width="1"/></svg>
      www.brightwateradvisory.example
    </div>
    <div class="contact-item">
      <svg viewBox="0 0 14 14"><path d="M3 1.5l2 3-1.2 1.4c.8 1.6 2 2.8 3.6 3.6L8.8 8.3l3 2-1 2.2C6 12 2 8 1.5 3z" fill="none" stroke="var(--gold)" stroke-width="1.3"/></svg>
      +0100 555 0142
    </div>
  </footer>
</main>
</body>
</html>
```